Asia Hotel need a card and logo

The new hotel in East Asia, Taiwan need a business card and logo design.The hotel's Chinese name is 岚柏文旅,English name is "Velmira Hotel".The core concept of this hotel is "Eco green", going to use many plant etc.,The building's first outlook draft is attached in the file for your reference.The style be modern and fashion will be good. Thank you.
Target Market(s)
East Asia
Industry/Entity Type
Hotel
Contact Information for Business Card
The hotel's name both in Chinese and English :岚柏商旅 Velmira Hotel
The logo, address, E-mail and tel number place.
Stuff's name and title.
Font styles to use
Colors
Designer to choose colors to be used in the design.
Look and feel
Each slider illustrates characteristics of the customer's brand and the style your logo design should communicate.

```html
<!DOCTYPE html>
<html lang="zh-Hant">
<head>
<meta charset="utf-8">
<title>岚柏商旅 Velmira Hotel — Business Card</title>
<link href="https://fonts.googleapis.com/css2?family=Didact+Gothic&family=Noto+Sans+TC:wght@300&display=swap" rel="stylesheet">
<style>
  :root {
    --page-bg: #eef0f0;
    --card-bg: #ffffff;
    --leaf-green: #9cec3c;
    --soft-green: #aee97d;
    --pale-green: #e8f6d6;
    --ink-grey: #9a9c9e;
  }
  * { margin: 0; padding: 0; box-sizing: border-box; }
  html, body {
    width: 1200px; height: 1200px; overflow: hidden;
    background: var(--page-bg);
    font-family: "Didact Gothic", sans-serif;
  }
  .canvas { position: relative; width: 1200px; height: 1200px; }
  .card {
    position: absolute; left: 238px; width: 708px; height: 393px;
    background: var(--card-bg);
  }
  .card--front { top: 94px; }
  .card--back { top: 685px; }

  .vertical-name {
    position: absolute; left: 32px; top: 70px;
    display: flex; flex-direction: column; gap: 36px;
    font-family: "Noto Sans TC", sans-serif; font-weight: 300;
    font-size: 36px; line-height: 36px; color: var(--soft-green);
  }

  .brand { position: absolute; display: flex; flex-direction: column; align-items: flex-start; }
  .brand__square { background: var(--leaf-green); }
  .brand__name { color: var(--ink-grey); text-transform: lowercase; }
  .brand__word { display: block; white-space: nowrap; }

  .brand--front { left: 306px; top: 180px; }
  .brand--front .brand__square { width: 104px; height: 104px; }
  .brand--front .brand__name { margin-top: 6px; }
  .brand--front .brand__word--main { font-size: 22px; line-height: 26px; letter-spacing: 0.1em; }
  .brand--front .brand__word--sub { font-size: 14px; line-height: 18px; letter-spacing: 0.72em; }

  .brand--back { left: 546px; top: 190px; }
  .brand--back .brand__square { width: 76px; height: 76px; }
  .brand--back .brand__name { margin-top: 6px; }
  .brand--back .brand__word--main { font-size: 16px; line-height: 19px; letter-spacing: 0.08em; }
  .brand--back .brand__word--sub { font-size: 11px; line-height: 14px; letter-spacing: 0.62em; }

  .stripe-panel {
    position: absolute; left: 466px; top: 72px; width: 216px; height: 250px;
    background: var(--pale-green);
  }

  .contact { position: absolute; left: 0; top: 88px; width: 716px; color: var(--ink-grey); }
  .contact__name {
    position: absolute; left: 0; top: 0; width: 716px;
    text-align: center; font-size: 18px; letter-spacing: 0.35em;
  }
  .contact__title {
    position: absolute; left: 0; top: 30px; width: 716px;
    text-align: center; font-size: 15px; letter-spacing: 0.3em;
  }
  .contact__list {
    position: absolute; left: 261px; top: 66px; list-style: none;
    font-size: 14px; letter-spacing: 0.08em; line-height: 23px;
  }
  .social { position: absolute; left: 294px; top: 270px; display: flex; gap: 19px; }
  .social__dot {
    width: 32px; height: 32px; border-radius: 50%;
    border: 1.5px solid var(--soft-green);
  }
</style>
</head>
<body>
<main class="canvas">
  <section class="card card--front">
    <div class="vertical-name" aria-label="岚柏商旅">
      <span>岚</span><span>柏</span><span>商</span><span>旅</span>
    </div>
    <div class="brand brand--front">
      <div class="brand__square"></div>
      <div class="brand__name">
        <span class="brand__word brand__word--main">Velmira</span>
        <span class="brand__word brand__word--sub">Hotel</span>
      </div>
    </div>
    <div class="stripe-panel" role="img" aria-label="Decorative vertical bamboo-like stripes in pale green"></div>
  </section>

  <section class="card card--back">
    <div class="contact">
      <p class="contact__name">Lina Ko</p>
      <p class="contact__title">CEO</p>
      <ul class="contact__list">
        <li>A: 12th Lane, Taiwan</li>
        <li>E: stay@velmira.tw</li>
        <li>P: 886-221-7340</li>
        <li>www.velmirahotel.com</li>
      </ul>
    </div>
    <div class="social" aria-label="Social media">
      <span class="social__dot"></span>
      <span class="social__dot"></span>
      <span class="social__dot"></span>
    </div>
    <div class="brand brand--back">
      <div class="brand__square"></div>
      <div class="brand__name">
        <span class="brand__word brand__word--main">Velmira</span>
        <span class="brand__word brand__word--sub">Hotel</span>
      </div>
    </div>
  </section>
</main>
</body>
</html>
```